Menu sign design for Italian Deli

Need designs for 2 hanging signs - one sided, full color, full bleed.
One sign finishes at 48" wide by 36" high, the other sign finishes at 24" wide by 36" high. (Copy and Specs included in PDF).

All files to be completed in PDF format, CMYK

Fonts, layout, colors, backgrounds, photos are totally up to you. Once we see some concepts we can give you more direction/ideas.
These signs will be used in an Italian Deli....(maybe pick-up the Italian colors?????)

```html
<!DOCTYPE html>
<html lang="en">
<head>
<meta charset="utf-8">
<title>Sub Menu</title>
<link rel="stylesheet" href="https://fonts.googleapis.com/css2?family=Oswald:wght@400;500;700&family=Roboto:wght@400;500&display=swap">
<style>
  :root {
    --green: #1f9c47;
    --band: #f1f2f1;
    --ink: #2a2a2a;
    --white: #ffffff;
    --soft: #a9dcb6;
  }
  * { margin: 0; padding: 0; box-sizing: border-box; }
  html, body { width: 849px; height: 1200px; overflow: hidden; background: var(--green); }
  .menu {
    position: relative; width: 849px; height: 1200px;
    background: var(--green); color: var(--white);
    font-family: "Roboto", Arial, sans-serif;
  }
  .menu-title {
    position: absolute; top: 8px; left: 0; width: 100%;
    text-align: center; font-family: "Oswald", sans-serif;
    font-weight: 700; font-size: 40px; letter-spacing: 1px; line-height: 48px;
  }
  .column-band {
    position: absolute; top: 58px; left: 0; width: 100%; height: 34px;
    background: var(--band); color: var(--ink);
    font-family: "Oswald", sans-serif; font-weight: 700; font-size: 22px;
  }
  .column-band span { position: absolute; top: 0; line-height: 34px; transform: translateX(-50%); }
  .price-block {
    position: absolute; top: 104px; width: 300px; transform: translateX(-50%);
    text-align: center; font-size: 14px; line-height: 20px;
  }
  .price-block .big { font-size: 16px; font-weight: 500; }
  .price-block .small { font-size: 12.5px; }
  .sub-list { position: absolute; top: 275px; left: 42px; width: 766px; list-style: none; }
  .sub-list li { display: flex; justify-content: space-between; align-items: baseline; height: 40px; }
  .sub-name { font-family: "Oswald", sans-serif; font-weight: 700; font-size: 20px; letter-spacing: .3px; }
  .sub-desc { font-size: 14px; color: var(--soft); }
  .extras { position: absolute; top: 836px; left: 0; width: 100%; text-align: center; }
  .extras-title { font-family: "Oswald", sans-serif; font-weight: 700; font-size: 21px; letter-spacing: .5px; margin-bottom: 8px; }
  .extras h3 { font-family: "Oswald", sans-serif; font-weight: 700; font-size: 15px; letter-spacing: .5px; margin-top: 10px; }
  .extras p { font-size: 13px; line-height: 22px; }
</style>
</head>
<body>
<main class="menu">
  <h1 class="menu-title">SUB MENU</h1>

  <div class="column-band">
    <span style="left:212px">HOT SUB</span>
    <span style="left:637px">COLD SUB</span>
  </div>

  <div class="price-block" style="left:212px">
    <div class="big">Round Roll &nbsp;$5.99</div>
    <div class="small">Medium (8") $8.99 Large (12") $9.99</div>
    <div class="big">Wraps &nbsp;$6.49</div>
    <div class="small">Ciabatta $6.99 Panini $6.99</div>
  </div>
  <div class="price-block" style="left:637px">
    <div class="big">Round Roll &nbsp;$5.99</div>
    <div class="small">Medium (8") $8.99 Large (12") $9.99</div>
    <div class="big">Wraps &nbsp;$6.49</div>
    <div class="small">Ciabatta $6.99 Panini $6.99</div>
  </div>

  <ul class="sub-list">
    <li><span class="sub-name">STEAK</span><span class="sub-desc">Cutlet, Nonna's Assorted (Ham, Turkey, Roast Beef)</span></li>
    <li><span class="sub-name">MEATBALL</span><span class="sub-desc">Nonna's Assorted (Ham, Turkey, Roast Beef)</span></li>
    <li><span class="sub-name">BLT</span><span class="sub-desc">Breaded Chicken Cutlet, Turkey, Roast Beef</span></li>
    <li><span class="sub-name">CHICKENPARM</span><span class="sub-desc">Breaded Chicken Cutlet, Ham, Turkey, Roast Beef</span></li>
    <li><span class="sub-name">ROASTBEEF</span><span class="sub-desc">Chicken Cutlet, Nonna's Assorted (Ham, Turkey, Roast Beef)</span></li>
    <li><span class="sub-name">SAUSAGE</span><span class="sub-desc">Breaded Chicken Cutlet, Ham, Turkey, Roast Beef</span></li>
    <li><span class="sub-name">SAUSAGEPARM</span><span class="sub-desc">Cutlet, Nonna's Assorted (Ham, Turkey, Roast Beef)</span></li>
    <li><span class="sub-name">CHICKENFRENCH</span><span class="sub-desc">Breaded Chicken, Ham, Turkey, Roast Beef</span></li>
    <li><span class="sub-name">CHICKENMARSALA</span><span class="sub-desc">Breaded Chicken, Assorted (Ham, Turkey, Roast Beef)</span></li>
    <li><span class="sub-name">PIZZA</span><span class="sub-desc">Nonna's Assorted (Ham, Turkey, Roast Beef)</span></li>
    <li><span class="sub-name">PASTRAMI</span><span class="sub-desc">Breaded Chicken Cutlet</span></li>
    <li><span class="sub-name">FRIEDBOLOGNA</span><span class="sub-desc">Breaded Chicken (Ham, Turkey, Roast Beef)</span></li>
    <li><span class="sub-name">HAMBURG</span><span class="sub-desc">Breaded Chicken Cutlet, Ham, Turkey</span></li>
    <li><span class="sub-name">CHEESEBURG</span><span class="sub-desc">Breaded Chicken Cutlet, Ham, Turkey, Roast Beef</span></li>
  </ul>

  <section class="extras">
    <h2 class="extras-title">ALL SUBS INCLUDE YOUR CHOICE OF THE FOLLOWING:</h2>
    <h3>VEGGIES:</h3>
    <p>Lettuce • Tomato • Onion • Hot Peppers •<br>
    Sweet Peppers • Dill or Sweet Pickles • Black Olives • Mushrooms • Cucumbers • Jalapeno Peppers</p>
    <h3>DRESSINGS:</h3>
    <p>Mayonnaise • Mustard • Italian Dressing • Oil •<br>
    Oil &amp; Vinegar • Honey Mustard • Spicy Mustard • Horseradish Sauce House Sauce<br>
    Sweet Glaze • Meat Hot Sauce • Steak Sauce • Ketchup • Hot Sauce • Blue Cheese</p>
    <h3>CHEESES:</h3>
    <p>Provolone • Mozzarella • American Swiss • Hot Pepper • Muenster</p>
  </section>
</main>
</body>
</html>
```